Stock Market Research Company Needs a new Design for our Podcast

We need a new logo and social media images for our podcast called Ledger Chat Podcast. We have a current design and logo but are looking to update the branding of the podcast. The podcast is highly interactive taking listener questions each week on individual stocks as well as stock portfolio building strategies.

Copy of Ledger Chat Podcast Thumbnail is our current branding.

Podcast Ad 2 Image attached for an idea of what we're looking for but using our specific colours.

Incorporate K from our current logo (attached)
Colours: Primary Color: (#1AA897), Secondary Color (#2E4151)
Clean/Modern style
Include Headshots of Hosts (images attached)

Target Market(s)

Podcast listeners and stock market investors

Industry/Entity Type

Investment

Logo Text

Title - Ledger Chat Podcast. Tagline - Stock Picks, Strategies & Tips For All Investors

Colors
33b8a4
86cfc6
00a990

Requirements
Must have
• Incorporate K from our current logo (attached)
Clean/Modern style

```html
<!DOCTYPE html>
<html lang="en">
<head>
<meta charset="utf-8">
<title>Ledger Chat Podcast Cover</title>
<link rel="stylesheet" href="https://fonts.googleapis.com/css2?family=Josefin+Sans:wght@400;700&display=swap">
<style>
  :root {
    --teal: #00a990;
    --teal-mid: #33b8a4;
    --teal-soft: #86cfc6;
    --teal-primary: #1aa897;
    --navy: #2e4151;
    --mint: #d8f0eb;
    --white: #ffffff;
    --stage: #eef1f0;
  }
  * { margin: 0; padding: 0; box-sizing: border-box; }
  html, body { width: 1200px; height: 1153px; overflow: hidden; background: var(--stage); }
  .cover {
    position: absolute; left: 40px; top: 16px;
    width: 1120px; height: 1120px; overflow: hidden;
    background: radial-gradient(circle at 50% 40%, var(--white) 0%, #eef8f6 45%, var(--mint) 100%);
    font-family: "Josefin Sans", sans-serif;
  }
  .cover-art { position: absolute; inset: 0; width: 1120px; height: 1120px; }
  .title-band {
    position: absolute; left: 0; top: 433px; width: 100%; height: 186px;
    background: var(--teal); border-top: 11px solid var(--navy);
    display: flex; align-items: center; justify-content: center;
  }
  .title {
    color: var(--white); font-weight: 700; font-size: 148px; line-height: 1;
    padding-top: 22px; letter-spacing: 0.01em;
    text-shadow: 3px 4px 5px rgba(0,0,0,0.35);
    white-space: nowrap;
  }
  .subtitle-band {
    position: absolute; left: 0; top: 619px; width: 100%; height: 140px;
    background: var(--navy); border-bottom: 12px solid var(--teal);
    display: flex; align-items: center; justify-content: center;
  }
  .subtitle {
    color: var(--white); font-weight: 700; font-size: 112px; line-height: 1;
    letter-spacing: 0.27em; margin-right: -0.27em; padding-top: 16px;
  }
  .tagline { list-style: none; }
  .tag {
    position: absolute; height: 60px; background: var(--teal-primary);
    color: var(--white); font-size: 36px; font-weight: 400;
    letter-spacing: 0.17em; display: flex; align-items: center; justify-content: center;
    padding-top: 6px; white-space: nowrap;
  }
  .tag-picks { left: 361px; top: 807px; width: 396px; }
  .tag-strategies { left: 361px; top: 892px; width: 396px; }
  .tag-tips { left: 232px; top: 977px; width: 654px; }
</style>
</head>
<body>
  <main class="cover">
    <svg class="cover-art" viewBox="0 0 1120 1120" xmlns="http://www.w3.org/2000/svg">
      <defs>
        <linearGradient id="host-tone" x1="0" y1="0" x2="0" y2="1">
          <stop offset="0" stop-color="#d9d6d2"/>
          <stop offset="1" stop-color="#b9aaa0"/>
        </linearGradient>
      </defs>

      <g class="hanger-lines" stroke="var(--navy)" stroke-width="6">
        <line x1="163" y1="0" x2="163" y2="433"/>
        <line x1="964" y1="0" x2="964" y2="433"/>
      </g>

      <g class="host host-left">
        <circle cx="163" cy="256" r="130" fill="var(--navy)"/>
        <circle cx="163" cy="256" r="120" fill="var(--teal-mid)"/>
        <g role="img" aria-label="Headshot of the first podcast host">
          <circle cx="163" cy="256" r="112" fill="url(#host-tone)"/>
        </g>
      </g>
      <g class="host host-right">
        <circle cx="964" cy="256" r="130" fill="var(--navy)"/>
        <circle cx="964" cy="256" r="120" fill="var(--teal-mid)"/>
        <g role="img" aria-label="Headshot of the second podcast host">
          <circle cx="964" cy="256" r="112" fill="url(#host-tone)"/>
        </g>
      </g>

      <g class="bar-chart bars-left">
        <rect x="251" y="413" width="28" height="20" fill="var(--teal-mid)"/>
        <rect x="289" y="360" width="28" height="73" fill="var(--teal-mid)"/>
        <rect x="327" y="371" width="28" height="62" fill="var(--teal-soft)"/>
        <rect x="364" y="309" width="28" height="124" fill="var(--teal-mid)"/>
        <rect x="402" y="288" width="28" height="145" fill="var(--teal-soft)"/>
      </g>
      <g class="bar-chart bars-right">
        <rect x="688" y="283" width="28" height="150" fill="var(--teal-mid)"/>
        <rect x="726" y="331" width="28" height="102" fill="var(--teal-soft)"/>
        <rect x="765" y="399" width="28" height="34" fill="var(--teal-mid)"/>
        <rect x="802" y="353" width="28" height="80" fill="var(--teal-soft)"/>
        <rect x="840" y="417" width="28" height="16" fill="var(--teal-mid)"/>
      </g>

      <g class="microphone">
        <path d="M481 239 V165 A78 78 0 0 1 637 165 V239 Z" fill="var(--teal-mid)"/>
        <path d="M481 239 H637 V300 A78 78 0 0 1 481 300 Z" fill="var(--navy)"/>
        <path d="M469 241 V300 A90 90 0 0 0 649 300 V241" fill="none" stroke="var(--navy)" stroke-width="10"/>
        <line x1="445" y1="241" x2="673" y2="241" stroke="var(--navy)" stroke-width="8"/>
        <rect x="441" y="233" width="6" height="16" fill="var(--navy)"/>
        <rect x="671" y="233" width="6" height="16" fill="var(--navy)"/>
        <rect x="553" y="390" width="12" height="43" fill="var(--navy)"/>
        <text x="559" y="318" text-anchor="middle" fill="var(--teal-mid)" font-family="Josefin Sans, sans-serif" font-weight="700" font-size="28" letter-spacing="1">LEDGER</text>
      </g>
    </svg>

    <header>
      <div class="title-band"><h1 class="title">LEDGER CHAT</h1></div>
      <div class="subtitle-band"><p class="subtitle">PODCAST</p></div>
    </header>

    <ul class="tagline">
      <li class="tag tag-picks">STOCK PICKS</li>
      <li class="tag tag-strategies">STRATEGIES</li>
      <li class="tag tag-tips">TIPS FOR ALL INVESTORS</li>
    </ul>
  </main>
</body>
</html>
```